Mezzanine Floor Manufacturer looking for a new business card design

We manufacture mezzanine floors and are providers of racking systems. We provide a range of items/services - simple rack repairs , full warehouse fit outs , manufacturer and install mezzanine floors , partitioning and large turnkey projects. Recently had a new website - www.corvane-shelving.co.uk and would like our business cards updating aswell . Our current card is single sided in the old logo colours (pdf attached) and needs updating.

Target Market(s)

We deal with large projects/ multi national companies and also smaller projects and companies throughout the UK ranging from a single warehouse to a large multi site company.

Industry/Entity Type

Business

Contact Information for Business Card

Will have job title,tel no's, email ,website address etc like example pdf

Requirements
Must have
• Hi - needs to use the colours of the logo & new website. Card needs to be professional

```html
<!DOCTYPE html>
<html lang="en">
<head>
<meta charset="utf-8">
<title>Corvane Shelving Ltd – Business Card</title>
<link href="https://fonts.googleapis.com/css2?family=Noto+Sans:wght@400;700&display=swap" rel="stylesheet">
<style>
  :root {
    --brand-red: #c0232a;
    --ink-grey: #4a4a4a;
    --soft-grey: #6d6a6b;
    --paper: #ffffff;
    --backdrop: #e4e4e6;
    --title-pink: #f2b9bb;
  }
  * { box-sizing: border-box; margin: 0; padding: 0; }
  html, body { width: 1200px; height: 780px; overflow: hidden; }
  body {
    background: var(--backdrop);
    font-family: "Noto Sans", Verdana, sans-serif;
    display: flex; align-items: center; justify-content: center; gap: 50px;
  }
  .card {
    position: relative; width: 540px; height: 310px;
    background: var(--paper);
    box-shadow: 0 6px 18px rgba(0,0,0,.18);
    overflow: hidden;
  }
  .brand-mark {
    position: absolute; display: flex; align-items: center; gap: 8px;
    color: var(--brand-red); font-weight: 700;
  }
  .brand-mark .dot { width: 16px; height: 16px; border-radius: 50%; background: var(--brand-red); }

  /* Reverse side */
  .card-back .company-name {
    position: absolute; left: 34px; top: 30px;
    color: var(--brand-red); font-weight: 700; font-size: 25px;
  }
  .card-back .brand-mark { right: 30px; top: 92px; font-size: 22px; }
  .services-heading {
    position: absolute; left: 50px; top: 82px;
    color: var(--brand-red); font-size: 19px;
  }
  .services-list {
    position: absolute; left: 66px; top: 112px;
    list-style: none; color: var(--ink-grey); font-size: 13px; line-height: 19px;
  }
  .services-list li::before {
    content: ""; display: inline-block; width: 5px; height: 5px; border-radius: 50%;
    background: var(--brand-red); margin: 0 12px 2px -17px; vertical-align: middle;
  }
  .address {
    position: absolute; left: 50px; top: 205px;
    font-style: normal; color: var(--soft-grey); font-size: 14px; line-height: 19px;
  }
  .address .web { color: var(--brand-red); }

  /* Front side */
  .card-front svg.sweep { position: absolute; inset: 0; }
  .card-front .brand-mark { right: 40px; top: 30px; font-size: 28px; }
  .card-front .company-name {
    position: absolute; right: 40px; top: 80px;
    color: var(--brand-red); font-weight: 700; font-size: 20px;
  }
  .contact-list {
    position: absolute; right: 40px; top: 120px;
    list-style: none; text-align: right; color: var(--ink-grey);
    font-size: 13.5px; line-height: 19px;
  }
  .contact-list li { display: flex; justify-content: flex-end; align-items: center; gap: 7px; }
  .contact-list svg { width: 10px; height: 10px; fill: var(--brand-red); }
  .person {
    position: absolute; left: 26px; bottom: 24px; color: var(--paper);
  }
  .person .name { font-weight: 700; font-size: 18px; letter-spacing: .5px; line-height: 24px; }
  .person .role { font-size: 15px; color: var(--title-pink); letter-spacing: .5px; line-height: 20px; }
</style>
</head>
<body>

  <section class="card card-back">
    <h1 class="company-name">Corvane Shelving Ltd</h1>
    <div class="brand-mark"><span class="dot"></span>Corvane</div>
    <h2 class="services-heading">Services</h2>
    <ul class="services-list">
      <li>simple rack repairs</li>
      <li>full warehouse fit outs</li>
      <li>manufacturer and install mezzanine floors</li>
      <li>partitioning and large turnkey projects</li>
    </ul>
    <address class="address">
      Twelve Mill Close<br>
      Ashcroft Business Park Ripton<br>
      Derbyshire DE7 4QA<br>
      <span class="web">www.corvane-shelving.co.uk</span>
    </address>
  </section>

  <section class="card card-front">
    <svg class="sweep" viewBox="0 0 540 310" width="540" height="310" aria-hidden="true">
      <path d="M150,0 C158,150 205,262 370,310 L0,310 L0,0 Z" fill="#c0232a"/>
      <path d="M163,-2 C172,140 220,245 385,300" fill="none" stroke="#6d6a6b" stroke-width="6"/>
    </svg>
    <div class="brand-mark"><span class="dot"></span>Corvane</div>
    <h1 class="company-name">Corvane Shelving Ltd</h1>
    <ul class="contact-list">
      <li>07700 900418 <svg viewBox="0 0 10 10"><rect x="2.5" y="0" width="5" height="10" rx="1"/></svg></li>
      <li>01632 960512 <svg viewBox="0 0 10 10"><path d="M1,3 Q5,0 9,3 L8,5 L6,4 L4,4 L2,5 Z M2,6 H8 V10 H2 Z"/></svg></li>
      <li>01632 960734 <svg viewBox="0 0 10 10"><rect x="0" y="3" width="10" height="6" rx="1"/><rect x="2" y="0" width="6" height="3"/></svg></li>
      <li>sales@corvane-shelving.co.uk <svg viewBox="0 0 10 10"><path d="M0,2 H10 V8 H0 Z M0,2 L5,6 L10,2" /></svg></li>
      <li>www.corvane-shelving.co.uk <svg viewBox="0 0 10 10"><circle cx="5" cy="5" r="5"/></svg></li>
    </ul>
    <div class="person">
      <div class="name">DALE WHITMORE</div>
      <div class="role">TECHNICAL SALES</div>
    </div>
  </section>

</body>
</html>
```